Tall Meadow Business card

We are a company that owns 2 compliance software programs for TV, Radio and Cable industries as well as an online job board. We need a professional business card that incorproates all three logos.

```html
<!DOCTYPE html>
<html lang="en">
<head>
<meta charset="utf-8">
<title>Tall Meadow Business Card</title>
<link href="https://fonts.googleapis.com/css2?family=Arimo:wght@400;700&family=Montserrat:wght@700;800&display=swap" rel="stylesheet">
<style>
  :root{
    --bg:#d9dadd;
    --paper:#ffffff;
    --red:#e8392b;
    --navy:#2e2a6b;
    --blue:#1a73c7;
    --ink:#3a3a3a;
    --grey:#8a8d93;
    --rule:#55557a;
  }
  *{margin:0;padding:0;box-sizing:border-box}
  html,body{width:1200px;height:895px;overflow:hidden}
  body{background:var(--bg);font-family:"Arimo",Arial,sans-serif;position:relative}
  .card{position:absolute;width:560px;height:320px;background:var(--paper);box-shadow:0 10px 26px rgba(0,0,0,.22);overflow:hidden}
  .card-front{left:60px;top:80px}
  .card-back{left:580px;top:490px}

  /* front */
  .brand-row{position:absolute;left:10px;right:10px;top:96px;height:90px;display:flex;align-items:center;justify-content:center}
  .brand{display:flex;align-items:center;gap:7px;padding:0 13px;font-family:"Montserrat",Arial,sans-serif;font-weight:800;font-size:15px;letter-spacing:-.2px;color:var(--navy);white-space:nowrap;flex:none}
  .brand-mark{width:12px;height:12px;border-radius:50%;background:var(--red);flex:none}
  .brand-jobs{color:var(--blue)}
  .brand-jobs .brand-mark{background:var(--blue)}
  .brand-divider{width:1.5px;height:70px;background:var(--navy);flex:none}
  .url-band{position:absolute;left:0;right:0;bottom:28px;height:28px;display:flex}
  .url-band span{flex:1;display:flex;align-items:center;justify-content:center;color:#fff;font-size:14px;white-space:nowrap}
  .url-band .u-red{background:var(--red)}
  .url-band .u-navy{background:var(--navy)}
  .url-band .u-blue{background:var(--blue)}

  /* back */
  .person{position:absolute;left:60px;top:150px;text-align:right;width:200px}
  .person-name{font-family:"Montserrat",Arial,sans-serif;font-weight:800;font-size:24px;color:var(--blue);white-space:nowrap}
  .person-title{font-size:15px;color:var(--ink);margin-top:2px}
  .back-rule{position:absolute;left:280px;top:80px;width:1.2px;height:150px;background:var(--rule)}
  .contact{position:absolute;left:300px;top:78px;list-style:none;font-size:14.5px;color:var(--ink);line-height:1.45}
  .contact li{display:flex;align-items:center;gap:8px;white-space:nowrap}
  .icon{width:16px;height:16px;flex:none}
  .back-stripe{position:absolute;left:0;right:0;bottom:0;height:22px}
</style>
</head>
<body>

<section class="card card-front">
  <div class="brand-row">
    <div class="brand"><span class="brand-mark"></span>Airwave Check</div>
    <div class="brand-divider"></div>
    <div class="brand"><span class="brand-mark"></span>Linecast Check</div>
    <div class="brand-divider"></div>
    <div class="brand brand-jobs"><span class="brand-mark"></span>CrewBoard</div>
  </div>
  <div class="url-band">
    <span class="u-red">www.airwavecheck.com</span>
    <span class="u-navy">www.linecastcheck.com</span>
    <span class="u-blue">www.crewboardjobs.com</span>
  </div>
</section>

<section class="card card-back">
  <div class="person">
    <div class="person-name">Ellis Warren</div>
    <div class="person-title">Managing Partner</div>
  </div>
  <div class="back-rule"></div>
  <ul class="contact">
    <li>48 Harbor Lane, Suite # 2</li>
    <li>Bristol, UK 30215</li>
    <li>
      <svg class="icon" viewBox="0 0 16 16"><circle cx="8" cy="8" r="7.5" fill="var(--red)"/><path d="M5 4.5l1.6-.4 1 2-1 .8c.5 1 1.3 1.8 2.3 2.3l.8-1 2 1-.4 1.6c-3.2 0-6.3-3.1-6.3-6.3z" fill="#fff"/></svg>
      555-010-2040
    </li>
    <li>
      <svg class="icon" viewBox="0 0 16 16"><circle cx="8" cy="8" r="7.5" fill="var(--red)"/><rect x="5.5" y="3.5" width="5" height="9" rx="1" fill="#fff"/><rect x="6.5" y="4.7" width="3" height="5.5" fill="var(--red)"/></svg>
      555-010-7788
    </li>
    <li>
      <svg class="icon" viewBox="0 0 16 16"><circle cx="8" cy="8" r="7.5" fill="var(--red)"/><rect x="4" y="5" width="8" height="6" fill="#fff"/><path d="M4 5l4 3.2L12 5" stroke="var(--red)" stroke-width="1" fill="none"/></svg>
      ellis.warren@tallmeadow.net
    </li>
    <li>
      <svg class="icon" viewBox="0 0 16 16"><circle cx="8" cy="8" r="7.5" fill="var(--red)"/><circle cx="8" cy="8" r="4" fill="none" stroke="#fff" stroke-width="1.1"/><ellipse cx="8" cy="8" rx="1.7" ry="4" fill="none" stroke="#fff" stroke-width="1"/><path d="M4 8h8" stroke="#fff" stroke-width="1"/></svg>
      www.crewboardjobs.com
    </li>
  </ul>
  <svg class="back-stripe" viewBox="0 0 560 22" preserveAspectRatio="none" aria-hidden="true">
    <polygon points="0,10 300,10 300,22 0,22" fill="var(--navy)"/>
    <polygon points="300,10 560,0 560,22 300,22" fill="var(--navy)"/>
    <polygon points="330,22 338,6 342,6 334,22" fill="var(--red)"/>
    <polygon points="346,22 354,5 556,0 560,0 560,22" fill="var(--blue)"/>
  </svg>
</section>

</body>
</html>
```